White Dove Release Postcard for Event Planners

We require a double-sided Postcard (8.5" x 5.5") that will be mailed to Event Planners advising them of our White Dove Release services for weddings, anniversaries, and other happy events.

Wingsong Moments is the originator of White Dove Releases in the greater Toronto area, adding a beautiful moment to weddings and other celebrations since 1995.

A professional release of Pure White Doves is a natural part of wedding ceremonies, lending a special celebratory note to the exchange of vows. White Doves are the living symbol of everlasting love, fidelity, peace and harmony. These lovely birds mate for life, building a home and raising their young together.

For more information, please visit www.wingsongmoments.example

Target Market(s)

Event and Wedding Planners. Primarily for weddings but could be for other types of celebratory events.

Industry/Entity Type

Events

Requirements
Must have
• Space for address label and stamp to be affixed.
• Pictures of beautiful brides with doves (see attachments).
Nice to have
• Multicultural weddings / brides
Should not have
• No religious images. Must be non-denominational.

```html
<!DOCTYPE html>
<html lang="en">
<head>
<meta charset="utf-8">
<title>Wingsong Moments Postcard</title>
<link rel="stylesheet" href="https://fonts.googleapis.com/css2?family=Open+Sans:wght@400;600;700&display=swap">
<style>
:root{
  --page:#ffffff;
  --ink:#1e1e1e;
  --ink-soft:#3a3a3a;
  --frame:#9a9a9a;
  --label:#2a2a2a;
  --sky-top:#c9dbf2;
  --sky-mid:#dce8f7;
  --sky-low:#eef4fb;
  --plume-deep:#cfcac6;
  --plume-mid:#e2dedb;
  --plume-light:#f3f1ef;
  --gown-light:#f4f2ea;
  --gown-mid:#dcd9cf;
  --suit-shade:#aeb9c8;
  --bird:#d9dbe0;
  --mail-line:#8c8c8c;
  --mail-fill:rgba(255,255,255,.85);
}
*{box-sizing:border-box;margin:0;padding:0}
html,body{width:1200px;height:1000px;overflow:hidden;background:var(--page)}
body{position:relative;font-family:"Open Sans",Arial,sans-serif;color:var(--ink)}
.card{position:absolute;left:94px;width:681px;overflow:hidden}
.card--front{top:42px;height:441px;border:1px solid var(--frame);background:var(--page)}
.card--back{top:518px;height:439px;background:linear-gradient(180deg,var(--sky-top) 0%,var(--sky-mid) 55%,var(--sky-low) 100%)}
.side-label{position:absolute;font-size:28px;font-weight:400;color:var(--label);letter-spacing:.5px}
.side-label--front{left:882px;top:218px}
.side-label--back{left:885px;top:705px}

.photo{position:absolute}
.photo--dove-hero{left:0;top:0;width:681px;height:441px;
  background:
    radial-gradient(ellipse 22% 30% at 80% 28%,var(--plume-deep) 0%,var(--plume-mid) 45%,rgba(226,222,219,0) 100%),
    radial-gradient(ellipse 45% 32% at 45% 38%,var(--plume-mid) 0%,var(--plume-light) 55%,rgba(243,241,239,0) 100%),
    radial-gradient(ellipse 20% 40% at 92% 75%,var(--plume-mid) 0%,rgba(226,222,219,0) 100%),
    var(--page)}
.photo--dove-small{left:160px;top:12px;width:115px;height:80px;border-radius:50%;
  background:radial-gradient(ellipse at 50% 50%,var(--bird) 0%,#e8eaee 40%,rgba(232,234,238,0) 72%)}
.photo--couple{left:0;top:165px;width:258px;height:274px;border-radius:60% 40% 0 0 / 35% 25% 0 0;
  background:
    radial-gradient(ellipse 55% 45% at 30% 75%,var(--gown-light) 0%,var(--gown-mid) 60%,rgba(220,217,207,0) 100%),
    radial-gradient(ellipse 45% 55% at 62% 70%,var(--gown-mid) 0%,var(--suit-shade) 70%,rgba(174,185,200,0) 100%)}

.mail-stamp{position:absolute;right:14px;top:14px;width:58px;height:68px;border:1.5px dashed var(--mail-line);background:var(--mail-fill)}
.mail-label{position:absolute;left:458px;top:200px;width:204px;height:120px;border:1.5px dashed var(--mail-line);background:var(--mail-fill)}

.brand{position:absolute;text-align:center;line-height:1}
.card--front .brand{left:20px;top:30px;width:316px}
.card--back .brand{left:264px;top:28px;width:400px}
.brand__group{font-size:11px;font-variant:small-caps;letter-spacing:.6px}
.brand__name{font-size:22px;font-weight:600;letter-spacing:2px;text-transform:uppercase;margin-top:5px}
.brand__services{font-size:9.5px;font-weight:700;font-variant:small-caps;letter-spacing:.4px;margin-top:5px}
.brand__since{font-size:9.5px;font-variant:small-caps;letter-spacing:.4px;margin-top:5px;color:var(--ink-soft)}
.contact-top{position:absolute;left:20px;top:104px;width:316px;text-align:center;font-size:11px;font-weight:600;line-height:14px}
.pitch{position:absolute}
.card--front .pitch{left:37px;top:212px;width:415px}
.pitch__heading{font-size:12px;font-weight:700}
.pitch__list{list-style:none;font-size:12px;line-height:15px;margin-top:14px}
.pitch__list li::before{content:"•";display:inline-block;width:16px}
.tagline{position:absolute;left:37px;top:355px;font-size:22.5px;line-height:28px;color:var(--ink)}
.back-copy{position:absolute;left:264px;top:98px;width:400px;text-align:center}
.back-copy .tagline-back{font-size:15.5px;line-height:20px}
.back-copy .pitch__heading{font-size:10.5px;margin-top:19px}
.back-copy .pitch__list{font-size:10.5px;line-height:13px;margin-top:10px}
.back-copy .pitch__list li::before{width:12px}
.back-copy p{font-size:10.5px;line-height:13px}
.care{margin-top:16px}
.reach{margin-top:13px}
.site{margin-top:13px;font-weight:700}
</style>
</head>
<body>
<section class="card card--front" aria-label="Postcard front">
  <div class="photo photo--dove-hero" role="img" aria-label="Photograph of a white dove in flight with wings spread"></div>
  <div class="mail-stamp" aria-label="Space for postage stamp"></div>
  <div class="mail-label" aria-label="Space for address label"></div>
  <div class="brand">
    <div class="brand__group">Silver Feather Group</div>
    <div class="brand__name">Wingsong Moments</div>
    <div class="brand__services">Weddings • Life Celebrations • Private &amp; Public Events</div>
    <div class="brand__since">Serving Southern Ontario Since 1995</div>
  </div>
  <div class="contact-top">www.wingsongmoments.example<br>416.555-0142</div>
  <div class="pitch">
    <h2 class="pitch__heading">Adding a special moment to special events for more than 15 years</h2>
    <ul class="pitch__list">
      <li>A natural part of wedding ceremonies... white doves mate for life</li>
      <li>Symbolizes everlasting love, fidelity, peace and harmony</li>
      <li>Animal-friendly and environmentally conscientious</li>
      <li>In keeping with today’s values and concerns</li>
      <li>Non-denominational; multi-cultural appeal</li>
      <li>Professional staff, always on time</li>
    </ul>
  </div>
  <p class="tagline">White Doves for Weddings and Other Celebrations<br>The memory of a White Dove Event lasts forever</p>
</section>
<div class="side-label side-label--front">FRONT</div>

<section class="card card--back" aria-label="Postcard back">
  <div class="photo photo--dove-small" role="img" aria-label="Photograph of a single white dove flying"></div>
  <div class="photo photo--couple" role="img" aria-label="Photograph of a bride and groom releasing doves with raised arms"></div>
  <div class="brand">
    <div class="brand__group">Silver Feather Group</div>
    <div class="brand__name">Wingsong Moments</div>
    <div class="brand__services">Weddings • Life Celebrations • Private &amp; Public Events</div>
    <div class="brand__since">Serving Southern Ontario Since 1995</div>
  </div>
  <div class="back-copy">
    <p class="tagline-back">White Doves for Weddingsand Other Celebrations<br>The memory of a White Dove Event lasts forever</p>
    <h2 class="pitch__heading">Adding a special moment to special events for more than 15 years</h2>
    <ul class="pitch__list">
      <li>A natural part of wedding ceremonies... white doves mate for life</li>
      <li>Symbolizes everlasting love, fidelity, peace and harmony</li>
      <li>Animal-friendly and environmentally conscientious</li>
      <li>In keeping with today’s values and concerns</li>
      <li>Non-denominational; multi-cultural appeal</li>
      <li>Professional staff, always on time</li>
      <li>Easy coordination with photographers/videographers</li>
    </ul>
    <p class="care">Our White Doves receive the best of care and are fully trained to return<br>to their dovecote upon their release from distances of more than<br>150 kilometres away.</p>
    <p class="reach">For more information, please contact Elena<br>info@wingsongmoments.example<br>416-555-0142</p>
    <p class="site">www.wingsongmoments.example</p>
  </div>
</section>
<div class="side-label side-label--back">BACK</div>
</body>
</html>
```